6 - 8 'Holistic' Instagram Graphics

Hi there!
We are looking to build up a library of Graphic Templates to use as Instagram & Facebook posts for our Holistic Medi Spa (& 3 other companies eventually)
This competition is for a sample of 6 - 8 designs. For the winner(s), we will make an agreement for a batch order (Looking for 200+ designs in total), and will be looking to make a long term arrangement.
Please find a full job description in the attached Word Document.
Any questions, don't hesitate to ask.
Thanks!
Medical Spa

```html
<!DOCTYPE html>
<html lang="en">
<head>
<meta charset="utf-8">
<title>Lumira Spa – Instagram Post Templates</title>
<link href="https://fonts.googleapis.com/css2?family=Montserrat:wght@400;500;600;700;800&family=Playfair+Display:ital,wght@0,500;0,600;1,600&family=Great+Vibes&display=swap" rel="stylesheet">
<style>
  :root{
    --mint:#c5e9e3;
    --mint-soft:#e3f5f2;
    --teal:#4fb0a4;
    --teal-dark:#2f8c82;
    --gold:#d6b574;
    --peach:#f0b49c;
    --ink:#2e3436;
    --grey:#7d8a8a;
    --white:#ffffff;
  }
  *{margin:0;padding:0;box-sizing:border-box}
  html,body{width:788px;height:1200px;overflow:hidden;background:var(--white)}
  body{position:relative;font-family:'Montserrat',sans-serif;color:var(--ink)}
  .post{position:absolute;width:322px;height:322px;overflow:hidden;background:var(--white);box-shadow:0 0 0 1px #eef2f1}
  .post *{position:absolute}
  .photo{display:block}
  .small{font-size:7px;line-height:1.45;color:var(--grey)}
  .caps{text-transform:uppercase;letter-spacing:.12em}

  /* Post 1 – Beauty Facemask */
  .p-facemask{left:38px;top:32px}
  .p-facemask .intro{left:30px;top:18px;width:190px}
  .p-facemask .photo{left:34px;top:44px;width:228px;height:128px;background:linear-gradient(135deg,#d9d4cf,#a9b4b6 55%,#e8e2dc)}
  .p-facemask .panel{left:0;top:150px;width:322px;height:172px;background:var(--mint)}
  .p-facemask .leaf-deco{left:14px;top:190px;width:90px;height:120px;background:radial-gradient(ellipse at 40% 60%,#a9d9d0,transparent 70%);opacity:.8}
  .p-facemask .dots{left:14px;top:60px;width:4px;height:60px;background:repeating-linear-gradient(var(--teal) 0 4px,transparent 4px 10px)}
  .p-facemask .bar{left:158px;top:244px;width:34px;height:14px;background:var(--gold)}
  .p-facemask .t1{left:198px;top:240px;font-size:20px;font-weight:500;letter-spacing:.1em}
  .p-facemask .t2{left:174px;top:264px;font-size:22px;font-weight:800;letter-spacing:.04em}

  /* Post 2 – Protect your skin */
  .p-protect{left:416px;top:32px;background:var(--mint)}
  .p-protect .title{right:20px;top:16px;text-align:right;font-family:'Playfair Display',serif;font-style:italic;font-weight:600;font-size:32px;line-height:1.05;color:var(--teal-dark)}
  .p-protect .intro{left:56px;top:36px;width:100px}
  .p-protect .offer{left:44px;top:88px;width:52px;height:52px;border-radius:50%;background:var(--peach);color:var(--white);font-size:10px;font-weight:700;text-align:center;padding-top:14px;line-height:1.2}
  .p-protect .arch{left:96px;top:100px;width:170px;height:222px;border-radius:85px 85px 0 0;background:linear-gradient(160deg,#e7d3c8,#b88f80 55%,#5a3f3b)}
  .p-protect .tag{left:-12px;top:200px;transform:rotate(-90deg);font-size:11px;color:var(--teal-dark);letter-spacing:.08em}
  .p-protect .rule{right:20px;top:140px;width:2px;height:150px;background:var(--white)}

  /* Post 3 – Treatment Promo */
  .p-promo{left:38px;top:434px}
  .p-promo .blob-a{left:150px;top:-30px;width:200px;height:170px;border-radius:55% 45% 60% 40%;background:var(--mint)}
  .p-promo .blob-b{left:-40px;top:100px;width:360px;height:180px;border-radius:50% 50% 40% 60%;background:var(--mint-soft)}
  .p-promo .photo{left:120px;top:20px;width:140px;height:120px;border-radius:60% 40% 55% 45%;background:linear-gradient(135deg,#f3e6de,#c7b2a6 60%,#8ea3a2)}
  .p-promo .ring{left:230px;top:70px;width:24px;height:24px;border-radius:50%;border:2px solid var(--gold)}
  .p-promo .h1{left:18px;top:176px;font-size:34px;font-weight:700;line-height:1}
  .p-promo .h2{left:18px;top:212px;font-size:34px;font-weight:700;line-height:1}
  .p-promo .script{left:24px;top:252px;font-family:'Great Vibes',cursive;font-size:26px;color:var(--gold)}
  .p-promo .note{left:34px;top:286px;font-size:8px;color:var(--ink)}
  .p-promo .web{right:18px;top:256px;font-size:7px;color:var(--grey)}

  /* Post 4 – Beauty Center */
  .p-center{left:416px;top:434px;background:var(--mint)}
  .p-center .frame{left:12px;top:12px;width:298px;height:298px;border:1.5px solid var(--white)}
  .p-center .photo{left:28px;top:40px;width:196px;height:244px;border-radius:50% 50% 45% 55%;background:linear-gradient(140deg,#f4e8e0,#d3b9a9 55%,#9ebfbb)}
  .p-center .title{right:24px;top:60px;text-align:right;font-family:'Playfair Display',serif;font-weight:500;font-size:24px;line-height:1.1}
  .p-center .offer{left:162px;top:196px;width:56px;height:56px;border-radius:50%;background:var(--peach);color:var(--white);font-size:12px;font-weight:700;text-align:center;padding-top:13px;line-height:1.2}
  .p-center .btn{right:24px;top:214px;padding:4px 8px;background:var(--peach);color:var(--white);font-size:7px;font-weight:700;white-space:nowrap}
  .p-center .contact{right:24px;top:260px;text-align:right}
  .p-center .lines{right:24px;top:296px;width:120px;height:6px;border-top:2px solid var(--peach);border-bottom:2px solid var(--peach)}
  .p-center .dot{left:40px;top:26px;width:8px;height:8px;border-radius:50%;background:var(--peach)}

  /* Post 5 – Massage Treatments */
  .p-massage{left:38px;top:834px}
  .p-massage .leaf-deco{left:0;top:0;width:322px;height:322px;background:radial-gradient(circle at 85% 20%,#d6efea,transparent 45%),radial-gradient(circle at 20% 10%,#e6f5f2,transparent 40%)}
  .p-massage .title{left:80px;top:34px;font-size:13px;font-weight:500;letter-spacing:.14em;color:var(--ink)}
  .p-massage .photo{left:0;top:120px;width:200px;height:202px;background:linear-gradient(150deg,#e9d6c8,#b89483 55%,#6b7d7e)}
  .p-massage .box{left:176px;top:100px;width:120px;height:70px;background:var(--white);border:1px solid var(--mint);font-size:9px;font-weight:700;line-height:1.5;padding:12px 10px;text-align:center}
  .p-massage .web{left:206px;top:290px;font-size:7px;color:var(--grey)}

  /* Post 6 – Love for Beauty */
  .p-love{left:416px;top:834px}
  .p-love .leaves{left:80px;top:-20px;width:170px;height:60px;border-radius:0 0 50% 50%;background:linear-gradient(180deg,#3f8a4a,#7fb77a)}
  .p-love .brand{left:0;width:322px;top:50px;text-align:center;font-size:10px;font-weight:700;letter-spacing:.18em;color:var(--teal-dark)}
  .p-love .title{left:0;width:322px;top:66px;text-align:center;font-family:'Great Vibes',cursive;font-size:40px;color:var(--teal-dark)}
  .p-love .sub{left:0;width:322px;top:118px;text-align:center;font-size:8px;font-weight:600;letter-spacing:.14em;color:var(--ink)}
  .p-love .photo{left:0;top:150px;width:322px;height:172px;background:linear-gradient(100deg,#e26d3e 0%,#e9b38f 25%,#dfe6df 50%,#9cc59a 75%,#f0f0ea 100%)}
</style>
</head>
<body>

<section class="post p-facemask">
  <div class="dots"></div>
  <p class="small intro">Gentle care for calm, radiant skin every single day.</p>
  <div class="panel"></div>
  <div class="photo" role="img" aria-label="Woman relaxing with a clay face mask at a spa"></div>
  <div class="leaf-deco" role="img" aria-label="Soft botanical leaf decoration"></div>
  <div class="bar"></div>
  <h2 class="t1">BEAUTY</h2>
  <h2 class="t2">FACEMASK</h2>
</section>

<section class="post p-protect">
  <p class="small intro">Daily care that keeps your skin soft and glowing.</p>
  <h2 class="title">Protect<br>your skin</h2>
  <div class="arch" role="img" aria-label="Woman with hands framing her face in an arched frame"></div>
  <div class="offer">20%<br>OFF</div>
  <span class="tag">#dailyroutine</span>
  <div class="rule"></div>
</section>

<section class="post p-promo">
  <div class="blob-b"></div>
  <div class="blob-a"></div>
  <div class="photo" role="img" aria-label="Woman receiving a facial treatment"></div>
  <div class="ring"></div>
  <h2 class="h1">Treatment</h2>
  <h2 class="h2">Promo</h2>
  <span class="script">Discount</span>
  <span class="note">20% for new year</span>
  <span class="web">www.lumiraspa.com</span>
</section>

<section class="post p-center">
  <div class="frame"></div>
  <div class="dot"></div>
  <div class="photo" role="img" aria-label="Woman receiving a skin care device treatment"></div>
  <h2 class="title">Beauty<br>Center</h2>
  <div class="offer">25%<br>OFF</div>
  <span class="btn caps">Book now</span>
  <p class="small contact">+123 456 7890<br>www.lumiraspa.com</p>
  <div class="lines"></div>
</section>

<section class="post p-massage">
  <div class="leaf-deco" role="img" aria-label="Faint tropical leaf background"></div>
  <h2 class="title">MASSAGE TREATMENTS</h2>
  <div class="photo" role="img" aria-label="Woman receiving a back massage"></div>
  <p class="box">DO YOU NEED<br>FIBER EVERY DAY?</p>
  <span class="web">www.lumiraspa.com</span>
</section>

<section class="post p-love">
  <div class="leaves" role="img" aria-label="Green leaves hanging from the top"></div>
  <span class="brand">LUMIRA SPA</span>
  <h2 class="title">Love for Beauty</h2>
  <span class="sub">EVERYTHING FOR YOUR BEAUTY</span>
  <div class="photo" role="img" aria-label="Natural spa products with citrus slices, towels and green clay"></div>
</section>

</body>
</html>
```